New Electrical Business advertisement

We Need an A4 flyer created advertising we are a new electrical company servicing this area. We need the flyer to stand out and have a friendly feel to it

Target Market(s)

Home owners and commerical business

Industry/Entity Type

Electrician

Font styles to use
Sans Serif

Requirements
Must have
• must stand out, be eye catching but have a professional feel

Must have company colours orange and blue
RBG Colours
BLUE: R:4 G:116 B:187
ORANGE: R:240 G:86 B:47

```html
<!DOCTYPE html>
<html lang="en">
<head>
<meta charset="utf-8">
<title>Ridgeline Electrical – Flyer</title>
<link rel="stylesheet" href="https://fonts.googleapis.com/css2?family=Montserrat:wght@700;800&family=Inter:wght@400&display=swap">
<style>
  :root {
    --blue: rgb(4,116,187);
    --orange: rgb(240,86,47);
    --white: #ffffff;
    --ink: #1c1c1c;
    --paper: #ffffff;
  }
  * { box-sizing: border-box; margin: 0; padding: 0; }
  html, body { width: 848px; height: 1200px; overflow: hidden; background: var(--paper); }
  .flyer { position: relative; width: 848px; height: 1200px; background: var(--paper); font-family: "Inter", Arial, sans-serif; color: var(--ink); }
  .brand { position: absolute; display: flex; align-items: center; justify-content: center; gap: 12px; }
  .brand-dot { width: 26px; height: 26px; border-radius: 50%; background: var(--orange); flex: none; }
  .brand-name { font-family: "Montserrat", Arial, sans-serif; font-weight: 700; color: var(--blue); line-height: 1.05; letter-spacing: 0.5px; }
  .brand--top { left: 55px; top: 70px; width: 315px; }
  .brand--top .brand-name { font-size: 30px; }
  .brand--bottom { left: 40px; top: 1080px; width: 250px; }
  .brand--bottom .brand-name { font-size: 22px; }
  .panel { position: absolute; color: var(--white); }
  .panel--philosophy { left: 24px; top: 216px; width: 386px; height: 255px; background: var(--blue); padding: 24px 24px 0 25px; }
  .panel-title { font-family: "Montserrat", Arial, sans-serif; font-weight: 700; font-size: 23px; letter-spacing: 0.3px; margin-bottom: 8px; white-space: nowrap; }
  .body-copy { font-size: 10.9px; line-height: 15.4px; text-align: justify; letter-spacing: -0.1px; }
  .photo { position: absolute; }
  .photo--repair { left: 429px; top: 40px; width: 394px; height: 431px; background: linear-gradient(135deg, #8a7b6a 0%, #4a3f36 45%, #2a2724 70%, #9d9892 100%); }
  .photo--electrician { left: 24px; top: 766px; width: 541px; height: 255px; background: linear-gradient(90deg, #cfc9bd 0%, #e2c9a8 35%, #6b6660 70%, #b7b4ad 100%); }
  .panel--about { left: 24px; top: 490px; width: 799px; height: 256px; background: var(--orange); }
  .about-col { position: absolute; width: 312px; }
  .about-col--left { left: 57px; top: 40px; }
  .about-col--left .panel-title { font-size: 18.5px; margin-bottom: 6px; }
  .about-col--right { left: 432px; top: 38px; }
  .panel--services { left: 565px; top: 766px; width: 258px; height: 422px; background: var(--blue); padding: 34px 0 0 36px; }
  .services-title { font-family: "Montserrat", Arial, sans-serif; font-weight: 800; font-size: 27px; line-height: 34px; letter-spacing: 0.5px; margin-bottom: 18px; }
  .service-list { list-style: none; }
  .service-item { display: flex; align-items: center; height: 55.5px; }
  .service-icon { width: 28px; height: 28px; flex: none; margin-right: 29px; }
  .service-label { font-size: 17px; line-height: 22px; }
  .contact { position: absolute; left: 309px; top: 1055px; width: 245px; font-size: 17px; line-height: 23px; color: var(--ink); font-style: normal; }
  .contact-line { display: flex; align-items: center; gap: 7px; white-space: nowrap; }
  .contact-line svg { width: 14px; height: 14px; flex: none; }
  .contact-address { margin-top: 6px; }
</style>
</head>
<body>
<main class="flyer">
  <div class="brand brand--top">
    <span class="brand-dot"></span>
    <span class="brand-name">RIDGELINE<br>ELECTRICAL</span>
  </div>

  <div class="photo photo--repair" role="img" aria-label="Photo: hands fitting a relay onto copper wiring inside an appliance"></div>

  <section class="panel panel--philosophy">
    <h2 class="panel-title">OUR PHILOSOPHY</h2>
    <p class="body-copy">Lorem ipsum dolor sit amet, consectetuer adipiscing elit, sed diam nonummy nibh euismod tincidunt ut laoreet dolore magna aliquam erat volutpat. Ut wisi enim ad minim veniam, quis nostrud exerci tation ullamcorper suscipit lobortis nisl ut aliquip ex ea commodo consequat. Duis autem vel eum iriure dolor in hendrerit in vulputate velit esse molestie consequat, vel illum dolore eu feugiat nulla facilisis at vero eros et accumsan et iusto odio dignissim qui blandit praesent luptatum zzril delenit augue duis dolore te feugait nulla facilisi.r in hendrerit in vulputate veesent luptatum zzril delenit augue duis dolore te feugait nulla facilisi.</p>
  </section>

  <section class="panel panel--about">
    <div class="about-col about-col--left">
      <h2 class="panel-title">RIDGELINE ELECTRICAL IS A</h2>
      <p class="body-copy">Lorem ipsum dolor sit amet, consectetuer adipiscing elit, sed diam nonummy nibh euismod tincidunt ut laoreet dolore magna aliquam erat volutpat. Ut wisi enim ad minim veniam, quis nostrud exerci tation ullamcorper suscipit lobortis nisl ut aliquip ex ea commodo consequat. Duis autem vel eum iriure dolor in hendrerit in vulputate velit esse molestie consequat, vel illum dolore eu feugiat nulla facilisis at vero eros et accumsan et iusto odio dignissim qui blandit praesent luptatum zzril delenit augue duis dolore te feugait nulla facilisi.</p>
    </div>
    <div class="about-col about-col--right">
      <p class="body-copy">Lorem ipsum dolor sit amet, consectetuer adipiscing elit, sed diam nonummy nibh euismod tincidunt ut laoreet dolore magna aliquam erat volutpat. Ut wisi enim ad minim veniam, quis nostrud exerci tation ullamcorper suscipit lobortis nisl ut aliquip ex ea commodo consequat. Duis autem vel eum iriure dolor in hendrerit in vulputate velit esse molestie consequat, vel illum dolore eu feugiat nulla facilisis at vero eros et accumsan et iusto odio dignissim qui blandit praesent luptatum zzril delenit augue duis dolore te feugait nulla facilero eros et accumsan et iusto odio dignissim qui blandit praesent luptatum zzril delenit augue duis dolor</p>
    </div>
  </section>

  <div class="photo photo--electrician" role="img" aria-label="Photo: smiling electrician in a yellow hard hat testing a switchboard"></div>

  <section class="panel panel--services">
    <h2 class="services-title">ELECTRICAL<br>SERVICES</h2>
    <ul class="service-list">
      <li class="service-item"><svg class="service-icon" viewBox="0 0 28 28"><circle cx="14" cy="14" r="11.5" fill="none" stroke="#fff" stroke-width="3"/><path d="M15.5 6.5 9.5 15h4l-1.5 6.5 6-8.5h-4z" fill="#fff"/></svg><span class="service-label">New<br>Installations</span></li>
      <li class="service-item"><svg class="service-icon" viewBox="0 0 28 28"><circle cx="14" cy="14" r="11.5" fill="none" stroke="#fff" stroke-width="3"/><path d="M15.5 6.5 9.5 15h4l-1.5 6.5 6-8.5h-4z" fill="#fff"/></svg><span class="service-label">Renovations<br>and Re-Wiring</span></li>
      <li class="service-item"><svg class="service-icon" viewBox="0 0 28 28"><circle cx="14" cy="14" r="11.5" fill="none" stroke="#fff" stroke-width="3"/><path d="M15.5 6.5 9.5 15h4l-1.5 6.5 6-8.5h-4z" fill="#fff"/></svg><span class="service-label">Installation and<br>Safety Switches</span></li>
      <li class="service-item"><svg class="service-icon" viewBox="0 0 28 28"><circle cx="14" cy="14" r="11.5" fill="none" stroke="#fff" stroke-width="3"/><path d="M15.5 6.5 9.5 15h4l-1.5 6.5 6-8.5h-4z" fill="#fff"/></svg><span class="service-label">Switchboard<br>upgrades</span></li>
      <li class="service-item"><svg class="service-icon" viewBox="0 0 28 28"><circle cx="14" cy="14" r="11.5" fill="none" stroke="#fff" stroke-width="3"/><path d="M15.5 6.5 9.5 15h4l-1.5 6.5 6-8.5h-4z" fill="#fff"/></svg><span class="service-label">Services and<br>breakdowns</span></li>
    </ul>
  </section>

  <div class="brand brand--bottom">
    <span class="brand-dot"></span>
    <span class="brand-name">RIDGELINE<br>ELECTRICAL</span>
  </div>

  <address class="contact">
    <div class="contact-line"><svg viewBox="0 0 14 14"><circle cx="7" cy="7" r="6.2" fill="none" stroke="#1c1c1c" stroke-width="1.2"/><path d="M4.6 3.8c.4-.3.8-.3 1 .1l.6 1.1c.2.4.1.7-.2.9l-.4.3c.4.9 1 1.5 1.9 1.9l.3-.4c.2-.3.5-.4.9-.2l1.1.6c.4.2.4.6.1 1-.8.9-1.7.9-3 .2-1.2-.7-2.2-1.7-2.8-2.9-.6-1.200-.5-2 .5-2.6z" fill="#1c1c1c"/></svg>555-014-2260</div>
    <div class="contact-line"><svg viewBox="0 0 14 14"><circle cx="7" cy="7" r="6.2" fill="#1c1c1c"/><rect x="3.5" y="4.6" width="7" height="4.8" fill="#fff"/><path d="M3.5 4.6 7 7.4l3.5-2.8" fill="none" stroke="#1c1c1c" stroke-width=".8"/></svg>hi@ridgelineco.com</div>
    <div class="contact-line"><svg viewBox="0 0 14 14"><circle cx="7" cy="7" r="6.2" fill="none" stroke="#1c1c1c" stroke-width="1.2"/><ellipse cx="7" cy="7" rx="2.6" ry="6.2" fill="none" stroke="#1c1c1c" stroke-width="1"/><path d="M1 7h12M2 4.2h10M2 9.8h10" stroke="#1c1c1c" stroke-width="1"/></svg>www.ridgelineco.com</div>
    <div class="contact-address">84 Harbor Lane,<br>Fairview, MA 02100</div>
  </address>
</main>
</body>
</html>
```